Retail Jewelry Business Card Design Project

We are in need of a new business card design for a retail jewelry store. This store is in the business of fine jewelry including but not specific to bridal jewelry, diamonds, designer jewelry and watches.

This store has been in business for 20 years but continues to strive for a modern professional appeal. The main colors use for this business are a royal blue, white and silver.

Target Market(s)

Target market is ages 18-50

Industry/Entity Type

Jewelry

Requirements
Must have
• Sales Person Name
Sales Person Email Address

Store Address
Store Phone
Website

Standard business card size. No odd shapes or sizes.
Nice to have
• Overall modern feel for card.

We have thought that a design with a nice feature of the logo on the back of the card would be nice but open to ideas.
Should not have
• No specific images of jewelry should be used.

```html
<!DOCTYPE html>
<html lang="en">
<head>
<meta charset="utf-8">
<title>Marlowe Hart Fine Jewelry – Business Card</title>
<link href="https://fonts.googleapis.com/css2?family=Arimo:wght@400;700&display=swap" rel="stylesheet">
<style>
  :root {
    --page: #ffffff;
    --royal-top: #3b3fc0;
    --royal-bottom: #2a2ea0;
    --silver: #8f8f98;
    --card-light: #cdcdcd;
    --ink-grey: #5e5e5e;
    --ink-soft: #666666;
    --accent-blue: #2f2f9a;
    --rule-violet: #7b6fd6;
  }
  html, body {
    margin: 0;
    width: 1200px;
    height: 848px;
    overflow: hidden;
    background: var(--page);
    font-family: "Arimo", Arial, sans-serif;
  }
  .canvas {
    position: relative;
    width: 1200px;
    height: 848px;
  }
  .card {
    position: absolute;
    border-radius: 8px;
    box-sizing: border-box;
    text-align: center;
  }
  /* Back of card */
  .card-back {
    left: 30px;
    top: 40px;
    width: 580px;
    height: 331px;
    background: linear-gradient(180deg, var(--royal-top) 0%, var(--royal-bottom) 100%);
    color: var(--silver);
  }
  .card-back .brand-name {
    margin-top: 40px;
    font-size: 40px;
    font-weight: 400;
    letter-spacing: 1px;
  }
  .card-back .ornament-area {
    width: 200px;
    height: 80px;
    margin: 34px auto 0;
    border-radius: 6px;
    background: linear-gradient(180deg, rgba(143,143,152,0.28), rgba(143,143,152,0.12));
  }
  .card-back .website {
    margin-top: 52px;
    font-size: 21px;
  }
  /* Front of card */
  .card-front {
    left: 590px;
    top: 460px;
    width: 580px;
    height: 331px;
    background: var(--card-light);
    color: var(--ink-grey);
  }
  .card-front .brand-name {
    margin-top: 34px;
    font-size: 34px;
    font-weight: 400;
    color: var(--accent-blue);
    letter-spacing: 1px;
  }
  .card-front .store-address {
    margin-top: 10px;
    font-size: 12px;
    line-height: 16px;
    color: var(--ink-soft);
  }
  .sales-name {
    display: flex;
    align-items: center;
    justify-content: center;
    gap: 14px;
    margin-top: 34px;
    font-size: 24px;
    font-weight: 700;
  }
  .sales-name .rule {
    width: 80px;
    height: 1.5px;
    background: var(--rule-violet);
  }
  .contact-line {
    display: flex;
    align-items: center;
    justify-content: center;
    gap: 6px;
    font-size: 15px;
    color: var(--ink-soft);
  }
  .contact-phone { margin-top: 22px; }
  .contact-email { margin-top: 16px; }
  .contact-line svg { fill: var(--accent-blue); }
</style>
</head>
<body>
<main class="canvas">

  <section class="card card-back" aria-label="Card back">
    <div class="brand-name">Marlowe Hart Fine Jewelry</div>
    <div class="ornament-area" role="img" aria-label="Pair of silver scroll flourishes"></div>
    <div class="website">www.marlowehartjewelry.com</div>
  </section>

  <section class="card card-front" aria-label="Card front">
    <div class="brand-name">Marlowe Hart Fine Jewelry</div>
    <div class="store-address">2230 Larkspur Avenue<br>Bayview, FL 32400</div>

    <div class="sales-name">
      <span class="rule"></span>
      <span>Marlowe Hart Benning</span>
      <span class="rule"></span>
    </div>

    <div class="contact-line contact-phone">
      <svg width="18" height="18" viewBox="0 0 24 24" aria-hidden="true">
        <path d="M6.6 10.8a15.2 15.2 0 0 0 6.6 6.6l2.2-2.2c.3-.3.7-.4 1-.2 1.1.4 2.3.6 3.6.6.6 0 1 .4 1 1V20c0 .6-.4 1-1 1C10.6 21 3 13.4 3 4c0-.6.4-1 1-1h3.5c.6 0 1 .4 1 1 0 1.3.2 2.5.6 3.6.1.3 0 .7-.2 1z"/>
      </svg>
      <span>xx xxx xxx xxx</span>
    </div>

    <div class="contact-line contact-email">
      <svg width="18" height="14" viewBox="0 0 24 18" aria-hidden="true">
        <path d="M0 0h24v18H0z M2 2v1l10 7 10-7V2z" fill-rule="evenodd"/>
      </svg>
      <span>marlowe@marlowehartjewelry.com</span>
    </div>
  </section>

</main>
</body>
</html>
```